Business card design needed

I need a business card for my Sydney Painting Business, that specialises in painting High -end residential homes. i want the design to look clean, modern and edgy. i also want a logo next to the RK Decorating, using RKD together.

Industry/Entity Type

Residential

Contact Information for Business Card

RK Decorating (business name),LIC 581062B, Rob Kellaway, robert.kellaway@fernmail.net, mobile 0412573068

```html
<!DOCTYPE html>
<html lang="en">
<head>
<meta charset="utf-8">
<title>RK Decorating – Business Card</title>
<link rel="stylesheet" href="https://fonts.googleapis.com/css2?family=Gelasio:wght@400&display=swap">
<style>
  :root {
    --page-bg: #e9e7e4;
    --card-center: #5a5a5a;
    --card-mid: #333333;
    --card-edge: #1c1c1c;
    --text-silver: #e4e4e4;
    --text-soft: #d2d2d2;
    --card-shadow: rgba(0, 0, 0, 0.35);
  }
  html, body {
    margin: 0;
    padding: 0;
    width: 1200px;
    height: 1181px;
    overflow: hidden;
    background: var(--page-bg);
  }
  .canvas {
    position: relative;
    width: 1200px;
    height: 1181px;
  }
  .business-card {
    position: absolute;
    left: 207px;
    top: 320px;
    width: 786px;
    height: 452px;
    border-radius: 26px;
    background: radial-gradient(ellipse 62% 70% at 50% 48%, var(--card-center) 0%, var(--card-mid) 55%, var(--card-edge) 100%);
    box-shadow: 0 6px 14px var(--card-shadow);
    overflow: hidden;
    font-family: "Gelasio", Georgia, serif;
    color: var(--text-silver);
    text-align: center;
  }
  .card-texture {
    position: absolute;
    inset: 0;
    background: radial-gradient(ellipse at 50% 40%, rgba(255,255,255,0.04), rgba(0,0,0,0) 70%);
  }
  .card-line {
    position: absolute;
    left: 0;
    width: 100%;
    margin: 0;
    font-weight: 400;
    line-height: 1;
  }
  .brand-lockup {
    position: absolute;
    left: 0;
    top: 218px;
    width: 100%;
    display: flex;
    justify-content: center;
    align-items: center;
    gap: 14px;
  }
  .brand-dot {
    width: 18px;
    height: 18px;
    border-radius: 50%;
    background: var(--text-silver);
  }
  .brand-name {
    margin: 0;
    font-size: 38px;
    line-height: 1;
    font-weight: 400;
    color: var(--text-silver);
  }
  .person-name {
    top: 326px;
    font-size: 26px;
    color: var(--text-silver);
  }
  .contact-mobile {
    top: 371px;
    font-size: 16px;
    color: var(--text-soft);
    letter-spacing: 0.5px;
  }
  .contact-email {
    top: 393px;
    font-size: 16px;
    color: var(--text-soft);
    letter-spacing: 0.3px;
  }
  .licence {
    top: 428px;
    font-size: 15px;
    color: var(--text-soft);
  }
</style>
</head>
<body>
<main class="canvas">
  <section class="business-card">
    <div class="card-texture" role="img" aria-label="Faint tonal damask pattern across the card face"></div>
    <div class="brand-lockup">
      <span class="brand-dot"></span>
      <p class="brand-name">RK Decorating</p>
    </div>
    <p class="card-line person-name">Rob Kellaway</p>
    <p class="card-line contact-mobile">Mobile :&nbsp; 0412573068</p>
    <p class="card-line contact-email">robert.kellaway@fernmail.net</p>
    <p class="card-line licence">LIC 581062B</p>
  </section>
</main>
</body>
</html>
```